KB Rubbish Removal Business Card

Hey,
I need a double sided business card designed for a rubbish removal business based in Australia. Logo is already chosen, similar colours preferred for both sides of the business card.

Details to include:

Front:

KB Rubbish Removal
Darren Holloway
Managing Director
Mobile: 0471 902 146
Email: darren@kbrubbishremoval.com.au
Website: kbrubbishremoval.com.au

Rear:

How did we do?
kbrubbishremoval.com.au/review

```html
<!DOCTYPE html>
<html lang="en">
<head>
<meta charset="utf-8">
<title>KB Rubbish Removal – Business Card</title>
<link rel="stylesheet" href="https://fonts.googleapis.com/css2?family=Roboto:wght@300;400;700&display=swap">
<style>
  :root {
    --backdrop: #58585a;
    --card: #ffffff;
    --ink: #4d4d4f;
    --brand: #2e9e48;
    --brand-light: #7cc242;
    --brand-dark: #157a3c;
  }
  * { margin: 0; padding: 0; box-sizing: border-box; }
  html, body {
    width: 1200px; height: 1200px; overflow: hidden;
    background: var(--backdrop);
    font-family: "Roboto", Arial, sans-serif;
    color: var(--ink);
  }
  .canvas { position: relative; width: 1200px; height: 1200px; }
  .card {
    position: absolute; left: 232px; width: 736px; height: 429px;
    background: var(--card); overflow: hidden;
  }
  .card--front { top: 186px; }
  .card--back { top: 666px; }
  .card__text { position: absolute; white-space: nowrap; line-height: 1; }

  .holder-name { left: 115px; top: 122px; font-size: 24.5px; font-weight: 700; letter-spacing: -0.2px; }
  .holder-role { left: 115px; top: 148px; font-size: 19px; font-weight: 300; }
  .contact { position: absolute; left: 115px; display: flex; align-items: center; gap: 7px;
             font-size: 19.5px; font-weight: 300; line-height: 1; }
  .contact svg { width: 14px; height: 14px; fill: var(--ink); flex: none; }
  .contact--phone { top: 206px; }
  .contact--web { top: 247px; }
  .contact--mail { top: 287px; }

  .brand-lockup {
    position: absolute; left: 474px; top: 194px;
    display: flex; align-items: center; gap: 10px;
  }
  .brand-lockup__dot {
    width: 38px; height: 38px; border-radius: 50%;
    background: var(--brand); flex: none;
  }
  .brand-lockup__name {
    font-size: 20px; font-weight: 700; color: var(--brand);
    white-space: nowrap; line-height: 1;
  }

  .brand-mark-area {
    position: absolute; left: -150px; top: 40px;
    width: 350px; height: 350px; border-radius: 50%;
    background: linear-gradient(135deg, var(--brand-light), var(--brand) 55%, var(--brand-dark));
  }

  .company-name { left: 301px; top: 162px; font-size: 24.5px; font-weight: 700; letter-spacing: -0.2px; }
  .review-heading { left: 299px; top: 191px; font-size: 45px; font-weight: 700; letter-spacing: -0.5px; }
  .review-link { left: 301px; top: 246px; font-size: 19.5px; font-weight: 300; }
</style>
</head>
<body>
<div class="canvas">

  <section class="card card--front" aria-label="Card front">
    <p class="card__text holder-name">Darren Holloway</p>
    <p class="card__text holder-role">Managing Director</p>
    <p class="contact contact--phone">
      <svg viewBox="0 0 14 14"><path d="M3.5 0h7a1 1 0 0 1 1 1v12a1 1 0 0 1-1 1h-7a1 1 0 0 1-1-1V1a1 1 0 0 1 1-1zm.5 1.5v9h6v-9zM7 11.5a.8.8 0 1 0 0 1.6.8.8 0 0 0 0-1.6z"/></svg>
      0471 902 146
    </p>
    <p class="contact contact--web">
      <svg viewBox="0 0 14 14"><path d="M7 0a7 7 0 1 0 0 14A7 7 0 0 0 7 0zm-1 1.2C5 2.4 4.5 4 4.4 6.3H1.3A5.8 5.8 0 0 1 6 1.2zm2 0a5.8 5.8 0 0 1 4.7 5.1H9.6C9.5 4 9 2.4 8 1.2zM6.4 1.5V6.3H5.5c.1-2 .4-3.5.9-4.8zm1.2 0c.5 1.3.8 2.8.9 4.8h-.9zM1.3 7.7h3.1c.1 2.3.6 3.9 1.6 5.1A5.8 5.8 0 0 1 1.3 7.7zm4.2 0h.9v4.8c-.5-1.3-.8-2.8-.9-4.8zm2.1 0h.9c-.1 2-.4 3.5-.9 4.8zm2 0h3.1A5.8 5.8 0 0 1 8 12.8c1-1.2 1.5-2.8 1.6-5.1z"/></svg>
      kbrubbishremoval.com.au
    </p>
    <p class="contact contact--mail">
      <svg viewBox="0 0 14 14"><path d="M0 3h14v8H0zm1.4 1 5.6 4 5.6-4zm-.4 1v5l3.5-2.6zm12 0L9.5 7.4 13 10zM5.4 8 1.5 10h11L8.6 8 7 9.2z"/></svg>
      darren@kbrubbishremoval.com.au
    </p>
    <div class="brand-lockup">
      <span class="brand-lockup__dot" aria-hidden="true"></span>
      <span class="brand-lockup__name">KB Rubbish Removal</span>
    </div>
  </section>

  <section class="card card--back" aria-label="Card back">
    <div class="brand-mark-area" role="img" aria-label="Company brand mark area"></div>
    <p class="card__text company-name">KB Rubbish Removal</p>
    <h1 class="card__text review-heading">How did we do?</h1>
    <p class="card__text review-link">kbrubbishremoval.com.au/review</p>
  </section>

</div>
</body>
</html>
```